ASSET BASED PROGRAM FLIER

Need flier to market hard money loan products offered HARD MONEY FIX & FLIP PROGRAMS

We offer a variety of loan programs Some program highlights include......

1) No Minimum Credit Score
2) 3-5 Day Close
3) Up to 100% of Purchase & Rehab
4) Rates as Low as 7%
5) Loans Offered Nationwide

Contact us today for more information at (800) 647-2915 x42 or email us at mwelton@brightlanefunding.example NMLS #731856 www.brightlanefunding.example

```html
<!DOCTYPE html>
<html lang="en">
<head>
<meta charset="utf-8">
<title>Hard Money Fix &amp; Flip Programs Flier</title>
<link rel="stylesheet" href="https://fonts.googleapis.com/css2?family=Montserrat:wght@300;400;600;700&display=swap">
<style>
  :root {
    --page: #ffffff;
    --navy: #111d45;
    --navy-deep: #0c1635;
    --mid-blue: #5aa3cd;
    --steel-blue: #3f6f9a;
    --pale-blue: #a9c8e0;
    --accent-blue: #5b9bd0;
    --list-blue: #4b8bc4;
    --heading-grey: #4a4a4a;
    --box-blue: #5d96c5;
    --white: #ffffff;
  }
  * { margin: 0; padding: 0; box-sizing: border-box; }
  html, body { width: 1200px; height: 1200px; overflow: hidden; background: var(--page); }
  body { font-family: "Montserrat", sans-serif; position: relative; }

  .flier {
    position: absolute; left: 204px; top: 41px;
    width: 792px; height: 1118px;
    overflow: hidden;
    background: var(--navy);
    box-shadow: 0 6px 24px rgba(0,0,0,0.18);
  }
  .hero-photo {
    position: absolute; left: 0; top: 0; width: 792px; height: 640px;
    background: linear-gradient(90deg, #d9c7a4 0%, #cdb891 35%, #e2d6bf 52%, #f4f3ee 56%, #f7f7f4 100%);
  }
  .waves { position: absolute; left: 0; top: 0; width: 792px; height: 1118px; }

  .call-line {
    position: absolute; left: 462px; top: 56px;
    font-weight: 700; font-size: 17px; letter-spacing: 1.2px;
    color: var(--accent-blue); white-space: nowrap;
  }
  .brand {
    position: absolute; left: 462px; top: 170px; width: 300px;
    display: flex; align-items: center; gap: 10px;
    font-weight: 600; font-size: 20px; color: var(--steel-blue);
  }
  .brand-dot { width: 22px; height: 22px; border-radius: 50%; background: var(--steel-blue); flex: none; }

  .program-title {
    position: absolute; right: 32px; top: 306px;
    text-align: right; font-weight: 700; font-size: 42px;
    line-height: 50px; letter-spacing: 1px; color: var(--heading-grey);
  }

  .loans-block { position: absolute; left: 74px; top: 790px; color: var(--white); }
  .loans-block .kicker { font-weight: 300; font-size: 37px; letter-spacing: 5px; line-height: 44px; }
  .loans-block .loans { font-weight: 300; font-size: 78px; letter-spacing: 7px; line-height: 88px; margin-top: 4px; }
  .loans-block .program { font-weight: 300; font-size: 35px; letter-spacing: 17px; line-height: 40px; }

  .contact-box {
    position: absolute; left: 116px; top: 1018px; width: 228px; height: 50px;
    background: var(--box-blue); color: var(--white);
    display: flex; flex-direction: column; justify-content: center; align-items: center;
    font-weight: 400; font-size: 10.5px; letter-spacing: 0.6px; line-height: 15px;
  }

  .highlights { position: absolute; left: 480px; top: 796px; width: 300px; }
  .highlights h2 {
    font-weight: 700; font-size: 26px; letter-spacing: 1.5px;
    color: var(--accent-blue); margin-left: 14px; margin-bottom: 20px;
  }
  .highlights ul { list-style: none; }
  .highlights li {
    position: relative; padding-left: 18px;
    font-size: 19px; line-height: 28px; color: var(--list-blue);
  }
  .highlights li::before {
    content: ""; position: absolute; left: 0; top: 11px;
    width: 6px; height: 6px; background: var(--list-blue);
  }
  .highlights li .wrap { display: block; padding-left: 29px; }
</style>
</head>
<body>
  <main class="flier">
    <div class="hero-photo" role="img" aria-label="Photo of a smiling construction worker in a yellow hard hat and safety vest leaning against a block wall at a building site"></div>

    <svg class="waves" viewBox="0 0 990 1398" preserveAspectRatio="none" aria-hidden="true">
      <defs>
        <linearGradient id="bandGrad" x1="0" y1="0" x2="1" y2="0">
          <stop offset="0" stop-color="#3c6a95"/>
          <stop offset="0.5" stop-color="#5aa3cd"/>
          <stop offset="1" stop-color="#2b4a78"/>
        </linearGradient>
        <radialGradient id="navyGrad" cx="0.35" cy="0.45" r="0.8">
          <stop offset="0" stop-color="#1a2a5c"/>
          <stop offset="1" stop-color="#0c1635"/>
        </radialGradient>
      </defs>
      <path d="M0,690 C260,800 560,640 990,610 L990,1398 L0,1398 Z" fill="#a9c8e0" opacity="0.85"/>
      <path d="M0,700 C220,820 520,720 990,645 L990,1398 L0,1398 Z" fill="url(#bandGrad)"/>
      <path d="M0,870 C140,990 360,950 600,880 C780,830 900,820 990,845 L990,1398 L0,1398 Z" fill="url(#navyGrad)"/>
    </svg>

    <p class="call-line">CALL US &nbsp;(800) 647-2915 x42</p>

    <div class="brand"><span class="brand-dot"></span><span>Brightlane Funding, Inc.</span></div>

    <h1 class="program-title">HARD MONEY<br>FIX &amp; FLIP<br>PROGRAMS</h1>

    <div class="loans-block">
      <p class="kicker">HARD MONEY</p>
      <p class="loans">LOANS</p>
      <p class="program">PROGRAM</p>
    </div>

    <div class="contact-box">
      <span>mwelton@brightlanefunding.example</span>
      <span>www.brightlanefunding.example</span>
    </div>

    <section class="highlights">
      <h2>HIGHLIGHTS</h2>
      <ul>
        <li>No Minimum Credit <span class="wrap">Score</span></li>
        <li>3-5 Day Close</li>
        <li>Up to 100% of <span class="wrap">Purchase &amp; Rehab</span></li>
        <li>Rates as Low as 7%</li>
        <li>Loans Offered <span class="wrap">Nationwide</span></li>
      </ul>
    </section>
  </main>
</body>
</html>
```